need label redone so i can edit it, it was ai generated.

Hey, this label design was originally generated by AI, and while I like the overall layout, there are several issues with it. Some elements are not lossless, others appear distorted, uneditable, or low quality.
What I need is a complete recreation of this label—exactly as it is—without adding any new creative touches. Please rebuild every element of the label from scratch, but make sure the final file is in a fully editable, high-resolution format (preferably an .ai file or equivalent).
Each part of the label (text, shapes, background, colors, etc.) should be separated into layers or components so I can easily change anything I want later—like the font, colors, text, or images.
Quality and editability are the top priorities here. Please make sure the design is 100% lossless and flexible for editing.

```html
<!DOCTYPE html>
<html lang="en">
<head>
<meta charset="utf-8">
<title>Surftail Dog Beach Towel Label</title>
<link rel="stylesheet" href="https://fonts.googleapis.com/css2?family=Fira+Sans+Condensed:wght@600;700;800&family=Kalam:wght@700&display=swap">
<style>
  :root {
    --page-bg: #ffffff;
    --sky-teal: #93d5d8;
    --wave-light: #a9dfe1;
    --wave-mid: #82ccd1;
    --navy: #074a6b;
    --cream: #f3e6d3;
    --orange: #e88a2d;
    --yellow: #f7d21e;
    --sand-light: #f3dba7;
    --sand-dark: #e6c487;
    --sea-deep: #1f8fa3;
    --sea-shallow: #6cc7cf;
    --coat-gold: #c9762a;
    --towel-teal: #1f8f98;
  }
  * { margin: 0; padding: 0; box-sizing: border-box; }
  html, body {
    width: 1200px; height: 768px; overflow: hidden;
    background: var(--page-bg);
  }
  .label {
    position: absolute; left: 330px; top: 24px;
    width: 540px; height: 720px; display: block;
  }
  .brand-name { font-family: "Fira Sans Condensed", sans-serif; font-weight: 800; fill: var(--navy); }
  .kicker { font-family: "Fira Sans Condensed", sans-serif; font-weight: 700; fill: var(--cream); }
  .headline { font-family: "Fira Sans Condensed", sans-serif; font-weight: 800; fill: var(--cream); }
  .tagline { font-family: "Kalam", cursive; font-weight: 700; fill: var(--yellow); }
  .badge-big { font-family: "Fira Sans Condensed", sans-serif; font-weight: 800; fill: var(--cream); }
  .badge-text { font-family: "Fira Sans Condensed", sans-serif; font-weight: 700; fill: var(--cream); }
  .closing-line { font-family: "Fira Sans Condensed", sans-serif; font-weight: 700; fill: var(--navy); }
  .feature-caption { font-family: "Fira Sans Condensed", sans-serif; font-weight: 700; fill: var(--navy); }
</style>
</head>
<body>
<svg class="label" viewBox="0 0 540 720" xmlns="http://www.w3.org/2000/svg">
  <defs>
    <linearGradient id="seaGrad" x1="0" y1="0" x2="0" y2="1">
      <stop offset="0" stop-color="var(--sea-deep)"/>
      <stop offset="1" stop-color="var(--sea-shallow)"/>
    </linearGradient>
    <linearGradient id="dogGrad" x1="0" y1="0" x2="0" y2="1">
      <stop offset="0" stop-color="var(--coat-gold)"/>
      <stop offset="0.45" stop-color="var(--coat-gold)"/>
      <stop offset="0.5" stop-color="var(--towel-teal)"/>
      <stop offset="1" stop-color="var(--towel-teal)"/>
    </linearGradient>
  </defs>

  <!-- background -->
  <g class="background">
    <rect width="540" height="720" fill="var(--sky-teal)"/>
    <path class="wave-band" d="M0 150 C120 120 260 170 540 110 L540 180 C300 220 150 170 0 200 Z" fill="var(--wave-light)"/>
    <path class="wave-band" d="M0 380 C150 350 330 400 540 360 L540 440 L0 440 Z" fill="var(--wave-mid)"/>
  </g>

  <!-- beach scene -->
  <rect class="sea-strip" x="0" y="432" width="540" height="80" fill="url(#seaGrad)" role="img" aria-label="Illustrated ocean with rolling waves meeting the shore"/>
  <path class="sand" d="M0 508 C180 520 360 505 540 480 L540 720 L0 720 Z" fill="var(--sand-light)"/>
  <path class="sand-footer" d="M0 632 L540 624 L540 720 L0 720 Z" fill="var(--sand-dark)"/>
  <path class="dog-illustration" d="M300 350 C330 330 420 330 450 360 L490 470 L490 640 C420 672 330 672 268 640 L268 470 Z" fill="url(#dogGrad)" role="img" aria-label="Illustration of a happy golden retriever wrapped in a teal beach towel on the sand"/>

  <!-- headline banner -->
  <path class="headline-banner" d="M60 190 C150 170 330 160 470 140 C492 137 500 150 500 175 L500 370 C520 372 540 376 540 378 L540 380 C420 360 200 420 80 392 C52 386 42 370 42 345 L42 220 C42 202 48 192 60 190 Z" fill="var(--navy)"/>

  <!-- brand -->
  <g class="brand">
    <circle cx="105" cy="63" r="17" fill="var(--navy)"/>
    <text class="brand-name" x="134" y="85" font-size="58" textLength="290" lengthAdjust="spacingAndGlyphs">SURFTAIL</text>
  </g>

  <!-- kicker pill -->
  <g class="kicker-pill" transform="rotate(-6 152 161)">
    <rect x="64" y="124" width="176" height="76" rx="38" fill="var(--orange)"/>
    <text class="kicker" x="152" y="158" font-size="22" text-anchor="middle">DRY YOUR DOG</text>
    <text class="kicker" x="152" y="184" font-size="22" text-anchor="middle">FASTER THAN EVER!</text>
  </g>

  <!-- headline -->
  <g class="headline-group" transform="rotate(-6 270 290)">
    <text class="headline" x="68" y="276" font-size="86" textLength="400" lengthAdjust="spacingAndGlyphs">DRY YOUR DOG</text>
    <text class="headline" x="86" y="338" font-size="86" textLength="360" lengthAdjust="spacingAndGlyphs">IN SECONDS</text>
    <text class="tagline" x="70" y="376" font-size="30" textLength="400" lengthAdjust="spacingAndGlyphs">The Ultimate Beach Towel for Dogs</text>
  </g>

  <!-- feature badges -->
  <g class="badge badge-absorbent">
    <circle cx="103" cy="459" r="51" fill="var(--orange)"/>
    <text class="badge-big" x="103" y="466" font-size="48" text-anchor="middle">5x</text>
    <text class="badge-text" x="103" y="484" font-size="17" text-anchor="middle">MORE</text>
    <text class="badge-text" x="103" y="501" font-size="17" text-anchor="middle">ABSORBENT</text>
  </g>
  <g class="badge badge-beachbag">
    <circle cx="195" cy="534" r="48" fill="var(--navy)"/>
    <text class="badge-text" x="195" y="524" font-size="20" text-anchor="middle">BEACH</text>
    <text class="badge-text" x="195" y="546" font-size="20" text-anchor="middle">BAG</text>
    <text class="badge-text" x="195" y="564" font-size="14" text-anchor="middle">MUST-HAVE</text>
  </g>
  <g class="badge badge-carride">
    <circle cx="99" cy="576" r="49" fill="var(--navy)"/>
    <text class="badge-text" x="99" y="564" font-size="19" text-anchor="middle">NO MORE</text>
    <text class="badge-text" x="99" y="586" font-size="19" text-anchor="middle">WET CAR</text>
    <text class="badge-text" x="99" y="608" font-size="19" text-anchor="middle">RIDES</text>
  </g>

  <!-- closing line -->
  <text class="closing-line" x="12" y="672" font-size="22">Trade the Stack of</text>
  <text class="closing-line" x="12" y="700" font-size="22">towels for One That Works.</text>

  <!-- care features -->
  <g class="feature feature-washable">
    <circle cx="415" cy="682" r="9" fill="none" stroke="var(--navy)" stroke-width="1.5"/>
    <rect x="410" y="677" width="10" height="10" rx="1.5" fill="none" stroke="var(--navy)" stroke-width="1.2"/>
    <circle cx="415" cy="683" r="2.5" fill="var(--navy)"/>
    <text class="feature-caption" x="415" y="697" font-size="5.5" text-anchor="middle">MACHINE</text>
    <text class="feature-caption" x="415" y="703" font-size="5.5" text-anchor="middle">WASHABLE</text>
  </g>
  <g class="feature feature-fastdry">
    <circle cx="442" cy="682" r="9" fill="none" stroke="var(--navy)" stroke-width="1.5"/>
    <path d="M442 675 C445 679 447 682 447 684 A5 5 0 0 1 437 684 C437 682 439 679 442 675 Z" fill="var(--navy)"/>
    <text class="feature-caption" x="442" y="697" font-size="5.5" text-anchor="middle">FAST</text>
    <text class="feature-caption" x="442" y="703" font-size="5.5" text-anchor="middle">DRYING</text>
  </g>
  <g class="feature feature-eco">
    <circle cx="469" cy="682" r="9" fill="none" stroke="var(--navy)" stroke-width="1.5"/>
    <path d="M469 676 C474 679 474 685 469 688 C464 685 464 679 469 676 Z M469 676 L469 690" fill="none" stroke="var(--navy)" stroke-width="1.2"/>
    <text class="feature-caption" x="469" y="697" font-size="5.5" text-anchor="middle">ECO</text>
    <text class="feature-caption" x="469" y="703" font-size="5.5" text-anchor="middle">FRIENDLY</text>
  </g>
</svg>
</body>
</html>
```